Renata Quisby

Luxury And Style -

Black - White & Gold

Target Market(s)

Fashion

Industry/Entity Type

Fashion

Requirements
Must have
• High-End
Nice to have
• We will Print on Silk Paper

```html
<!DOCTYPE html>
<html lang="en">
<head>
<meta charset="utf-8">
<title>Renata Quisby Letterhead</title>
<link href="https://fonts.googleapis.com/css2?family=Lato:wght@400;700&family=Poppins:wght@300;400&display=swap" rel="stylesheet">
<style>
  :root {
    --backdrop: #dedede;
    --paper: #ffffff;
    --gold: #b8905f;
    --gold-light: #d2ac7c;
    --navy: #020322;
    --ink: #141414;
    --body-text: #6f6f6f;
    --date-text: #7a7a7a;
  }
  * { box-sizing: border-box; margin: 0; padding: 0; }
  html, body {
    width: 1168px; height: 1200px; overflow: hidden;
    background: var(--backdrop);
  }
  .letterhead {
    position: absolute; left: 177px; top: 40px;
    width: 813px; height: 1120px;
    background: var(--paper);
    box-shadow: 0 4px 18px rgba(0,0,0,0.18);
    overflow: hidden;
  }
  .brand {
    position: absolute; left: 86px; top: 56px; width: 200px;
    text-align: center;
  }
  .brand-dot {
    display: block; width: 34px; height: 34px; margin: 0 auto 14px;
    border-radius: 50%; background: var(--gold);
  }
  .brand-name {
    font-family: "Poppins", sans-serif; font-weight: 300;
    font-size: 17px; letter-spacing: 3.2px; color: var(--ink);
    text-transform: uppercase; white-space: nowrap;
  }
  .brand-tagline {
    margin-top: 2px;
    font-family: "Poppins", sans-serif; font-weight: 300;
    font-size: 10px; color: var(--ink); letter-spacing: 0.2px;
  }
  .contact {
    position: absolute; left: 564px; top: 58px;
    padding-left: 10px; border-left: 1.5px solid var(--gold);
    font-family: "Poppins", sans-serif; font-weight: 300;
    font-size: 13px; line-height: 18px; color: var(--ink);
  }
  .contact-address { margin-bottom: 4px; }
  .contact-line { display: flex; align-items: center; gap: 5px; line-height: 17.5px; }
  .contact-line svg { width: 10px; height: 10px; flex: none; }
  .salutation {
    position: absolute; left: 73px; top: 310px;
    font-family: "Lato", sans-serif; font-weight: 700;
    font-size: 16px; line-height: 19.5px; color: var(--ink);
  }
  .letter-date {
    position: absolute; right: 72px; top: 331px;
    font-family: "Lato", sans-serif; font-size: 12px; color: var(--date-text);
  }
  .letter-body {
    position: absolute; left: 73px; top: 390px; width: 668px;
    font-family: "Lato", sans-serif; font-size: 11.9px;
    line-height: 19.4px; color: var(--body-text);
    text-align: justify; hyphens: auto;
  }
  .letter-body p + p { margin-top: 19px; }
  .signature {
    position: absolute; left: 73px; top: 900px;
    width: 172px; height: 36px;
    background: linear-gradient(90deg, #ececec, #f6f6f6);
    border-radius: 4px;
  }
  .footer-wave {
    position: absolute; left: 0; bottom: 0;
    width: 813px; height: 136px;
  }
</style>
</head>
<body>
  <main class="letterhead">
    <header class="brand">
      <span class="brand-dot"></span>
      <div class="brand-name">Renata Quisby</div>
      <div class="brand-tagline">LUXURY AND STYLE</div>
    </header>

    <address class="contact" style="font-style:normal">
      <div class="contact-address">48 Carrow Lane, Suite 5<br>Hollin Bay, NY 10478</div>
      <div class="contact-line">
        <svg viewBox="0 0 10 10"><path d="M1 4 Q5 0 9 4 L8 5 L7 3.6 Q5 3 3 3.6 L2 5Z M2.5 5 H7.5 L8.5 9 H1.5Z" fill="var(--gold)"/></svg>
        <span>+1 555 204 7810</span>
      </div>
      <div class="contact-line">
        <svg viewBox="0 0 10 10"><rect x="0.5" y="2" width="9" height="6" fill="var(--gold)"/><path d="M0.5 2 L5 5.5 L9.5 2" stroke="#fff" stroke-width="0.8" fill="none"/></svg>
        <span>hello@renataquisby.com</span>
      </div>
      <div class="contact-line">
        <svg viewBox="0 0 10 10"><circle cx="5" cy="5" r="4.5" fill="var(--gold)"/><path d="M0.5 5 H9.5 M5 0.5 Q2 5 5 9.5 M5 0.5 Q8 5 5 9.5" stroke="#fff" stroke-width="0.6" fill="none"/></svg>
        <span>www.renataquisby.com</span>
      </div>
    </address>

    <div class="salutation">Dear.<br>Mrs Dora Ellis Pratt</div>
    <div class="letter-date">Date: 06-october-2025</div>

    <section class="letter-body">
      <p>Lorem ipsum dolor sit amet, consectetur adipiscing elit, sed do eiusmod tempor incididunt ut labore et dolore magna aliqua. Sollicitudin ac orci phasellus egestas tellus rutrum tellus. Euismod elementum nisi quis eleifend quam adipiscing vitae proin sagittis. Egestas sed tempus urna et pharetra pharetra. Quis blandit turpis cursus in hac habitasse. Sed velit dignissim sodales ut eu. Ac auctor augue mauris augue neque. In arcu cursus euismod quis viverra nibh cras pulvinar mattis. Libero justo laoreet sit amet. Felis eget nunc lobortis mattis aliquam faucibus purus in. Pulvinar etiam non quam lacus suspendisse faucibus. Odio tempor orci dapibus ultrices. Velit dignissim sodales ut eu sem integer vitae justo. Fermentum et sollicitudin ac orci phasellus egestas. Pharetra vel turpis nunc eget lorem dolor sed. Sed turpis tincidunt id aliquet risus feugiat in ante. Mus mauris vitae ultricies leo integer malesuada nunc vel. Rhoncus urna neque viverra justo nec ultrices dui. Ut placerat orci nulla pellentesque dignissim enim sit amet.</p>
      <p>Bibendum arcu vitae elementum curabitur vitae nunc. Nunc pulvinar sapien et ligula ullamcorper malesuada. At elementum eu facilisis sed. Erat pellentesque adipiscing commodo elit at imperdiet dui accumsan sit. Nunc scelerisque viverra mauris in aliquam sem fringilla. In vitae turpis massa sed. Volutpat ac tincidunt vitae semper quis lectus nulla at. Massa placerat duis ultricies lacus sed turpis. Dui vivamus arcu felis bibendum ut tristique et egestas. Blandit aliquam etiam erat velit scelerisque in dictum non consectetur. Id neque aliquam vestibulum morbi blandit cursus risus at. Sed egestas egestas fringilla phasellus faucibus scelerisque eleifend donec. Ornare quam viverra orci sagittis eu volutpat odio facilisis. Volutpat sed cras ornare arcu dui vivamus arcu. Interdum consectetur libero id faucibus nisl.</p>
      <p>Viverra mauris in aliquam sem. Mattis molestie a iaculis at erat pellentesque adipiscing commodo elit. Sit amet volutpat consequat mauris nunc. Aliquam nulla facilisi cras fermentum. Sed turpis tincidunt id aliquet risus feugiat. Augue neque gravida in fermentum et sollicitudin ac orci.</p>
    </section>

    <div class="signature" role="img" aria-label="Handwritten signature of the sender"></div>

    <svg class="footer-wave" viewBox="0 0 1196 200" preserveAspectRatio="none" aria-hidden="true">
      <defs>
        <linearGradient id="goldSweep" x1="0" x2="1" y1="0" y2="0">
          <stop offset="0" stop-color="var(--gold-light)"/>
          <stop offset="0.55" stop-color="var(--gold)"/>
          <stop offset="1" stop-color="var(--gold-light)"/>
        </linearGradient>
      </defs>
      <path d="M0 84 C250 172 600 162 850 138 C1000 124 1120 126 1196 146 V200 H0Z" fill="var(--navy)"/>
      <path d="M10 82 C250 150 560 140 850 98 C1000 76 1120 88 1196 135 C1100 104 1000 100 860 116 C600 148 250 158 10 82Z" fill="url(#goldSweep)"/>
    </svg>
  </main>
</body>
</html>
```